Need a professional card design. Ostervane building company specialise in residential and commercial builds. New homes, additions & renovations.
Wanting a card with creativity and professionalism.
Want card that utilises logo.

Back and front.

I have just created a logo, and want to use it on the business card.
Attached a copy of the logo.
Attached is also a current business card which I wish to redesign

please utilise both sides

Residential

• Reg# 58306

```html
<!DOCTYPE html>
<html lang="en">
<head>
<meta charset="utf-8">
<title>Ostervane Building Co – Business Card</title>
<link rel="stylesheet" href="https://fonts.googleapis.com/css2?family=Barlow:wght@400;500;600&family=Source+Sans+3:wght@400;700&display=swap">
<style>
  :root {
    --paper: #ffffff;
    --ink: #111111;
    --label: #1a1a1a;
    --muted: #6b6b6b;
    --orange: #fa963c;
    --rule: #8a8a8a;
    --on-orange: #ffffff;
  }
  * { margin: 0; padding: 0; box-sizing: border-box; }
  html, body { width: 1200px; height: 849px; overflow: hidden; background: var(--paper); }
  .sheet { position: relative; width: 1200px; height: 849px; font-family: "Barlow", sans-serif; }
  .sheet-title {
    position: absolute; left: 36px; top: 32px;
    font-family: "Source Sans 3", sans-serif; font-size: 18.5px; color: var(--ink); font-weight: 700;
  }
  .sheet-title span { font-weight: 400; }
  .side-label {
    position: absolute; top: 212px; width: 485px; text-align: center;
    font-family: "Source Sans 3", sans-serif; font-size: 19px; color: var(--label);
  }
  .side-label.front { left: 78px; }
  .side-label.back { left: 639px; }
  .card {
    position: absolute; top: 263px; width: 486px; height: 315px;
    border: 1px solid var(--rule);
  }
  .card-front { left: 78px; background: var(--paper); }
  .card-back { left: 639px; background: var(--orange); }

  .brand {
    position: absolute; left: 0; right: 0; top: 92px; text-align: center;
    font-family: "Barlow", sans-serif; font-weight: 500; color: var(--ink);
  }
  .brand-name { display: block; font-size: 50px; letter-spacing: 2px; line-height: 1; }
  .brand-sub { display: block; font-size: 19px; letter-spacing: 6px; margin-top: 16px; line-height: 1; }
  .services {
    position: absolute; left: 0; right: 0; top: 235px; text-align: center;
    font-size: 15.5px; color: var(--muted); letter-spacing: 0.6px; line-height: 20px;
  }

  .contact {
    position: absolute; left: 40px; top: 53px; color: var(--on-orange);
    font-size: 17px; line-height: 22px; letter-spacing: 0.3px;
  }
  .contact .name { font-weight: 600; }
  .contact .block { margin-bottom: 24px; }
  .contact .reg { font-size: 15px; margin-top: 1px; }
  .corner-mark {
    position: absolute; left: 385px; top: 40px; width: 58px; height: 58px;
    background: var(--on-orange);
  }
</style>
</head>
<body>
<main class="sheet">
  <h1 class="sheet-title">BUSINESS CARD (<span>size 85x55mm)</span></h1>

  <p class="side-label front">Front Side</p>
  <p class="side-label back">Back Side</p>

  <section class="card card-front" aria-label="Card front">
    <div class="brand">
      <span class="brand-name">OSTERVANE</span>
      <span class="brand-sub">BUILDING CO</span>
    </div>
    <p class="services">NEW HOMES - ADDITIONS &amp; RENOVATIONS<br>DOMESTIC &amp; COMMERCIAL BUILDINGS</p>
  </section>

  <section class="card card-back" aria-label="Card back">
    <div class="contact">
      <p class="block"><span class="name">DORIAN VALCOTT</span> DIRECTOR<br>0400 512 938</p>
      <p class="block">42 HARWICK LANE<br>ELDERTON, WA 6099<br>T 08 9100 2846<br>F 08 9100 2847<br>OSTERVANEBUILDING@MAIL.COM</p>
      <p class="reg">REG.NO 58306</p>
    </div>
    <div class="corner-mark" aria-hidden="true"></div>
  </section>
</main>
</body>
</html>
```